KM Group

We need a new website for our company and since we had a very good work done for our logo in this site, we're back for the entire job.

Our company name is Halvorsen Capital Group. We're adding files of examples of what we have done today. In my opinion we need a more attention lock in the site but yet financial simple work.

Our files (attached) will let you know what we have so far. We need a complete change but the colours should be the same, however you can change them not running away to far from the original, and of course matching with the logo.

We need examples for 3 kind of layouts.

- A HOME welcome layout
- An internal Layout with sidebar
- And internal Layout wide

We can buy image licenses if needed for assets.
Actually there are 5 slide images placed on the Welcome HOME, we need those there, but you can improve with better images to match the new website!!!

Target Market(s)

Clients looking for financial advisers, tax and funds specialist, currency advisers

Industry/Entity Type

Financial

Requirements
Must have
• all the fonts must be in accordance with the financial market sites........the welcome home page must be precise, neat and information accurate........the menu should be elegant........main focus on the Home page, should be also the PRIVATE ACCESS box log in.......

```html
<!DOCTYPE html>
<html lang="en">
<head>
<meta charset="utf-8">
<title>Halvorsen Capital Group</title>
<link href="https://fonts.googleapis.com/css2?family=Arimo:wght@400;700&family=Cinzel:wght@700&display=swap" rel="stylesheet">
<style>
:root{
  --orange:#ec7421;
  --orange-dark:#c85a12;
  --ink:#222;
  --text:#333;
  --grey:#777;
  --dark:#3d3d3d;
  --darker:#2b2b2b;
  --line:#ddd;
  --up:#2fbf2f;
}
*{margin:0;padding:0;box-sizing:border-box}
html,body{width:849px;height:1200px;overflow:hidden;background:#fff;font-family:Arimo,Arial,sans-serif;color:var(--text)}
.page{position:relative;width:849px;height:1200px;background:#fff}
.abs{position:absolute}
.head-title{font-family:Cinzel,Georgia,serif;font-weight:700;color:var(--orange)}
.topline{left:0;top:0;width:849px;height:2px;background:var(--orange)}
.header{left:0;top:2px;width:849px;height:88px;background:linear-gradient(#fff,#f2f2f2)}
.brand{left:100px;top:16px;display:flex;align-items:center;gap:6px}
.brand-mark{width:14px;height:14px;background:var(--orange)}
.brand-name{font-family:Arimo,Arial,sans-serif;font-weight:700;font-size:14px;color:var(--ink);letter-spacing:.5px;line-height:1.1}
.utility{right:106px;top:9px;display:flex;gap:22px;font-size:9px;color:#555}
.utility span{display:flex;align-items:center;gap:5px}
.phone{right:102px;top:33px;font-size:13px;font-weight:700;color:var(--ink);display:flex;align-items:center;gap:6px}
.nav{left:286px;top:61px;display:flex;gap:0;font-size:9px;font-weight:700;color:#333}
.nav a{padding:4px 10px;text-decoration:none;color:inherit}
.nav a.active{background:var(--orange);color:#fff;border-radius:2px;padding:4px 12px;margin-right:0}
.hero{left:0;top:90px;width:849px;height:296px;background:linear-gradient(90deg,#dfe8f2 0%,#c8d6e6 30%,#6f85a3 55%,#2c3b58 75%,#3d4e6c 100%)}
.hero-copy{left:130px;top:152px;width:280px}
.hero-copy h2{font-size:17px;letter-spacing:.3px;margin-bottom:8px}
.hero-copy p{font-size:12px;font-weight:700;color:#333;line-height:19px;letter-spacing:.3px}
.btn{display:inline-flex;align-items:center;gap:6px;background:var(--orange);color:#fff;font-weight:700;border-radius:3px}
.hero-btn{left:134px;top:284px;font-size:10px;padding:5px 6px 5px 6px}
.arrow{width:26px;height:26px;border-radius:50%;background:rgba(90,90,90,.75);color:#fff;font-size:14px;display:flex;align-items:center;justify-content:center}
.access{left:563px;top:355px;width:186px;height:162px;background:linear-gradient(#f08a3a,#d7661c);border:1px solid #c9c9c9;box-shadow:0 4px 6px rgba(0,0,0,.2)}
.access-head{height:31px;background:linear-gradient(#4a4a4a,#2c2c2c);color:#fff;font-family:Cinzel,Georgia,serif;font-weight:700;font-size:16px;display:flex;align-items:center;justify-content:center;letter-spacing:.5px}
.field{position:absolute;left:6px;width:172px;height:23px;background:#fff;border:1px solid #d9d9d9;border-radius:2px;font-size:8px;color:#333;padding:6px 6px}
.forgot{position:absolute;left:8px;top:110px;font-size:8px;color:#fff}
.login{position:absolute;right:6px;top:130px;background:#2a2a2a;color:#fff;font-size:9px;font-weight:700;padding:3px 10px;border-radius:2px}
.welcome{left:101px;top:404px;width:422px}
.welcome h1{font-size:16px;padding-bottom:4px;border-bottom:1px solid var(--line)}
.welcome h1 b{color:var(--ink)}
.welcome p{font-size:8px;line-height:13.2px;margin-top:8px;color:#333;text-align:justify}
.more-btn{left:459px;top:502px;font-size:8.5px;padding:4px 9px}
.divider{left:100px;top:539px;width:650px;height:1px;background:var(--line)}
.col{top:558px;width:180px}
.col h3{font-size:11px;margin-bottom:6px}
.col .ph{height:88px;border-radius:2px;box-shadow:0 3px 4px rgba(0,0,0,.2)}
.col p{font-size:7.5px;line-height:14px;color:#444;margin-top:9px;padding-left:3px}
.col .rm{display:block;text-align:right;font-size:7.5px;font-weight:700;color:#222;text-decoration:underline;margin-top:8px}
.vsep{top:568px;width:1px;height:160px;background:#e6e6e6}
.ticker{left:98px;top:772px;width:651px;height:33px;background:linear-gradient(#5a5a5a,#333);border-radius:2px;display:flex;box-shadow:0 3px 4px rgba(0,0,0,.25)}
.tick{display:flex;align-items:center;padding:0 12px;font-size:7.5px;font-weight:700;color:#fff;border-right:1px solid #222;gap:4px;white-space:nowrap}
.tick:last-child{border-right:none}
.up{color:var(--up)}
.dn{color:var(--orange)}
.verified{left:100px;top:841px;width:650px;text-align:center;font-size:11px}
.verified-line{left:100px;top:862px;width:650px;height:1px;background:var(--line)}
.badges{left:230px;top:876px;display:flex;gap:56px;align-items:center}
.badge{background:#d8d8d8}
.footer{left:0;top:940px;width:849px;height:182px;background:linear-gradient(#4a4a4a,#3a3a3a)}
.fcol{top:951px}
.fcol h4{font-size:10px;padding-bottom:4px;border-bottom:1px dashed #777;margin-bottom:8px}
.fcol ul{list-style:none}
.fcol li{font-size:7.5px;color:#ddd;padding-left:12px;position:relative;margin-bottom:9px}
.fcol.tight li{margin-bottom:5.5px}
.fcol.mid li{margin-bottom:7.5px}
.fcol li::before{content:"";position:absolute;left:0;top:2px;border-left:3px solid #bbb;border-top:2.5px solid transparent;border-bottom:2.5px solid transparent}
.bottom{left:0;top:1122px;width:849px;height:78px;background:var(--darker)}
.bottom p{position:absolute;left:101px;top:14px;width:646px;font-size:7.5px;line-height:12px;color:#ccc;text-align:justify}
.bottom .copy{top:62px;text-align:center;left:0;width:849px;font-size:7.5px}
</style>
</head>
<body>
<div class="page">
  <div class="abs topline"></div>
  <header class="abs header"></header>
  <div class="abs brand"><span class="brand-mark"></span><span class="brand-name">HALVORSEN CAPITAL<br>GROUP</span></div>
  <div class="abs utility">
    <span><svg width="11" height="11" viewBox="0 0 11 11"><rect x="1" y="2" width="8" height="8" fill="none" stroke="#ec7421" stroke-width="1.3"/><path d="M5 6 L10 1" stroke="#ec7421" stroke-width="1.3"/></svg>Apply Now</span>
    <span><svg width="13" height="10" viewBox="0 0 13 10"><rect x=".5" y=".5" width="12" height="9" fill="none" stroke="#ec7421"/><path d="M.5 .5 L6.5 5.5 L12.5 .5" fill="none" stroke="#ec7421"/></svg>Contact Us</span>
  </div>
  <div class="abs phone"><svg width="17" height="17" viewBox="0 0 17 17"><circle cx="8.5" cy="8.5" r="7.5" fill="none" stroke="#ec7421" stroke-width="1.5"/><path d="M6 4.5 L7.5 6.5 L6.8 7.6 Q7.8 9.6 9.5 10.3 L10.5 9.5 L12.5 11 L11.5 12.5 Q7 12 4.8 6 Z" fill="#ec7421"/></svg>123-456-7890</div>
  <nav class="abs nav"><a class="active">HOME</a><a>ABOUT US</a><a>INVESTMENTS</a><a>FUNDS</a><a>BROKERAGE</a><a>EXCHANGE</a><a>ACCOUNTS</a></nav>

  <section class="abs hero" role="img" aria-label="Photo of business colleagues in suits reviewing documents at an office desk"></section>
  <div class="abs hero-copy">
    <h2 class="head-title">Teamwork for your Benefit</h2>
    <p>Aliquam erat volutpat. Ut wisi enim adi minim veniam, quis nostrud exerciateiu tation ullamcorper suscipit lobortis nisl ut aliquip ex ea commodo consequatito Duis autem vel eum iriure dolor.</p>
  </div>
  <div class="abs btn hero-btn">READ MORE <svg width="13" height="13" viewBox="0 0 13 13"><circle cx="6.5" cy="6.5" r="6" fill="#fff"/><path d="M5 3.8 L9 6.5 L5 9.2Z" fill="#ec7421"/></svg></div>
  <div class="abs arrow" style="left:99px;top:202px">&lt;</div>
  <div class="abs arrow" style="left:721px;top:197px">&gt;</div>

  <div class="abs access">
    <div class="access-head">Private Access</div>
    <div class="field" style="top:45px">AC. Number</div>
    <div class="field" style="top:79px">AC. Password</div>
    <div class="forgot">forgot acc number / password?</div>
    <div class="login">Login</div>
  </div>

  <section class="abs welcome">
    <h1 class="head-title">Welcome to <b>Halvorsen Capital</b></h1>
    <p>Lorem ipsum dolor sit amet consectetur adipisicing elitsed do eiusmod tempor incididunt ut labore et dolore magna aliqua. Ut enim ad minim veniam, quis nostrud exercitation ullamco laboris nisi ut aliquip ex ea commodo consequat. Duis aute irure dolor in reprehenderit in voluptate velit esse cillum dolore eu fugiat nulla pariatur. Excepteur sint occaecat cupidatat non proident, sunt in culpa qui officia deserunt mollit anim id est laborum. Lorem ipsum dolor sit amet consectetur adipisicing elitsed do eiusmod.</p>
  </section>
  <div class="abs btn more-btn">Read More</div>
  <div class="abs divider"></div>

  <div class="abs col" style="left:101px">
    <h3 class="head-title">Management &amp; Strategy</h3>
    <div class="ph" role="img" aria-label="Photo of hands with a pen over a printed bar chart" style="background:linear-gradient(#f4f4f4,#d9dcdf)"></div>
    <p>Lorem ipsum dolor sit amet, consectetuer adipi iscing elit, sed diam nonummy nibh euismodtin cidunt ut laoreet dolore magna aliquam erat vot.</p>
    <a class="rm">Read More »</a>
  </div>
  <div class="abs vsep" style="left:307px"></div>
  <div class="abs col" style="left:335px">
    <h3 class="head-title">Funds</h3>
    <div class="ph" role="img" aria-label="Image of a blue world map overlaid with market figures" style="background:linear-gradient(135deg,#1d6fc4,#5fb0ee)"></div>
    <p>Lorem ipsum dolor sit amet, consectetuer adipi iscing elit, sed diam nonummy nibh euismodtin cidunt ut laoreet dolore magna aliquam erat vot.</p>
    <a class="rm">Read More »</a>
  </div>
  <div class="abs vsep" style="left:541px"></div>
  <div class="abs col" style="left:560px">
    <h3 class="head-title">Currency Exchange</h3>
    <div class="ph" role="img" aria-label="Image of green buy and red sell keyboard keys" style="background:linear-gradient(90deg,#2e9a2e 0%,#3cb03c 48%,#c01818 52%,#d42a2a 100%)"></div>
    <p>Lorem ipsum dolor sit amet, consectetuer adipi iscing elit, sed diam nonummy nibh euismodtin cidunt ut laoreet dolore magna aliquam erat vot.</p>
    <a class="rm">Read More »</a>
  </div>

  <div class="abs ticker">
    <div class="tick" style="width:117px">GBP/UAH = <span class="up">12.65761 ▲</span></div>
    <div class="tick" style="width:129px">GBP/UGX = <span class="dn">4010.06174 ▼</span></div>
    <div class="tick" style="width:112px">GBP/USD = <span class="up">1.55817 ▲</span></div>
    <div class="tick" style="width:121px">GBP/UYU = <span class="up">34.36026 ▲</span></div>
    <div class="tick" style="width:78px">GBP/VEF = <span class="dn">0</span></div>
    <div class="tick" style="width:94px">GBP/VUV = <span class="up">151.7</span></div>
  </div>

  <div class="abs verified head-title">Verified and Protected by</div>
  <div class="abs verified-line"></div>
  <div class="abs badges">
    <div class="badge" style="width:62px;height:26px;border-radius:13px"></div>
    <div class="badge" style="width:58px;height:22px"></div>
    <div class="badge" style="width:30px;height:30px;border-radius:50%"></div>
    <div class="badge" style="width:52px;height:20px"></div>
  </div>

  <footer class="abs footer"></footer>
  <div class="abs fcol mid" style="left:100px;width:68px"><h4 class="head-title">About Us</h4><ul><li>History</li><li>Expertize</li><li>Idedtity</li><li>Strategy</li><li>Contact Us</li></ul></div>
  <div class="abs fcol tight" style="left:193px;width:150px"><h4 class="head-title">Investments</h4><ul><li>Term Deposits</li><li>Management &amp; Strategy</li><li>Client Relations</li><li>Financial Privacy</li><li>Tax Advice</li><li>Wealth Analysis &amp; Financial Planning</li><li>Active Advisory Group</li><li>Manager Selection Services</li><li>Private Equity</li></ul></div>
  <div class="abs fcol mid" style="left:378px;width:97px"><h4 class="head-title">Funds</h4><ul><li>Overview</li><li>Administration</li><li>Funds Security</li><li>Core Services</li><li>Reporting</li><li>Revenue Opportunities</li><li>How it works?</li><li>Glossary</li></ul></div>
  <div class="abs fcol mid" style="left:504px;width:136px"><h4 class="head-title">Currency Exchange</h4><ul><li>Foreign Exchange</li><li>Fx Forword</li><li>Fx Options</li></ul></div>
  <div class="abs fcol mid" style="left:504px;top:1053px;width:136px"><h4 class="head-title">Accounts</h4><ul><li>Apply Now</li><li>Private Access</li></ul></div>
  <div class="abs fcol mid" style="left:665px;width:83px"><h4 class="head-title">Brokerage</h4><ul><li>Institutional</li><li>Research</li><li>Trading</li></ul></div>

  <div class="abs bottom">
    <p>Lorem ipsum dolor sit amet, consectetuer elit, sed diam nonummy nibh euismod tincidunt ut laoreet dolore magna aliquam erat volutpat. Ut wisi enim ad minim veniam, quis nostrud exerci tation ullamcorper suscipit lobortis nisl ut aliquip ex ea commodo consequat. Duis autem vel eum iriure dolor in hendrerit in vulputate velit esse molestie consequat, vel illum dolore eu feugiat nulla facilisis at vero eros et accumsan et iusto odio dignissim qui blandit praesent luptatum zzril delenit augue duis dolore te facilisi.</p>
    <p class="copy">© 2013 HalvorsenCapitalGroup &nbsp;|&nbsp; All Rights Reserved</p>
  </div>
</div>
</body>
</html>
```